Larkspur Ridge Management - Business Cards

I need business cards. My current logo was designed by a designer at this site and I very much like and am happy with the results. I would like a business card that is trendy, unique, current yet professional. I deal with high net worth clients daily

Target Market(s)

Out of state investors looking to get into the rental market in Ohio

Industry/Entity Type

Property Management, Consulting

Contact Information for Business Card

Name, Title (Chief Financial Officer) office phone number (555) 817-3094 website address larkridgemgmt.example

Font styles to use
Sans Serif

Colors
0054AA
0677BA
7BADD7
CADEEF
E8F1F8
0094D4
00A9DD
6FCCEA
C7EBF8
E9F6FB
00AB8E
00BBA5
67D7C9
C6EFE9
E9F9F6

```html
<!DOCTYPE html>
<html lang="en">
<head>
<meta charset="utf-8">
<title>Larkspur Ridge Management – Business Cards</title>
<link rel="stylesheet" href="https://fonts.googleapis.com/css2?family=Montserrat:wght@400;700;800&family=Open+Sans:wght@400&display=swap">
<style>
  :root {
    --backdrop: #154f91;
    --card-dark: #060708;
    --card-light: #ffffff;
    --navy: #22325a;
    --red: #c8202e;
    --white: #ffffff;
    --rule-dark: #1e1e1e;
  }
  * { box-sizing: border-box; margin: 0; padding: 0; }
  html, body {
    width: 1200px; height: 1200px; overflow: hidden;
    background: var(--backdrop);
  }
  .canvas { position: relative; width: 1200px; height: 1200px; }
  .card {
    position: absolute; left: 293px; width: 612px; height: 367px; overflow: hidden;
  }
  .card--front { top: 190px; background: var(--card-dark); }
  .card--back { top: 600px; background: var(--card-light); }

  .brand-name {
    position: absolute; width: 200px;
    display: flex; align-items: center; gap: 10px;
    font-family: "Montserrat", sans-serif; font-weight: 700;
    font-size: 21px; line-height: 1.15; text-transform: uppercase;
  }
  .brand-name__mark { flex: none; width: 14px; height: 14px; }
  .card--front .brand-name { left: 42px; top: 145px; color: var(--white); }
  .card--front .brand-name__mark { background: var(--red); }
  .card--back .brand-name { left: 42px; top: 130px; color: var(--navy); }
  .card--back .brand-name__mark { background: var(--red); }

  .divider { position: absolute; width: 2px; }
  .card--front .divider { left: 272px; top: 93px; height: 160px; background: var(--red); }
  .card--back .divider { left: 254px; top: 86px; height: 160px; background: var(--rule-dark); }

  .services {
    position: absolute; left: 289px; top: 131px;
    font-family: "Montserrat", sans-serif; font-weight: 400;
    font-size: 28px; line-height: 27.5px; color: var(--white);
    text-transform: uppercase;
  }

  .person { position: absolute; left: 274px; top: 83px; }
  .person__name {
    font-family: "Montserrat", sans-serif; font-weight: 800;
    font-size: 29px; line-height: 32px; color: var(--navy); text-transform: uppercase;
  }
  .person__title {
    font-family: "Montserrat", sans-serif; font-weight: 400;
    font-size: 20px; line-height: 26px; color: var(--red);
  }

  .contact-list { position: absolute; left: 280px; top: 166px; list-style: none; }
  .contact-list__item {
    display: flex; align-items: center; height: 24.5px;
    font-family: "Open Sans", sans-serif; font-size: 18px; color: var(--navy);
  }
  .contact-list__icon { width: 22px; height: 22px; margin-right: 11px; flex: none; }

  .base-band {
    position: absolute; left: 0; bottom: 0; width: 100%; height: 28px; background: var(--navy);
  }
</style>
</head>
<body>
<main class="canvas">

  <section class="card card--front" aria-label="Card front">
    <div class="brand-name"><span class="brand-name__mark"></span><span>Larkspur Ridge Management</span></div>
    <div class="divider"></div>
    <p class="services">Property<br>Management<br>Consulting</p>
  </section>

  <section class="card card--back" aria-label="Card back">
    <div class="brand-name"><span class="brand-name__mark"></span><span>Larkspur Ridge Management</span></div>
    <div class="divider"></div>
    <div class="person">
      <h1 class="person__name">Marcus Ellery</h1>
      <p class="person__title">Chief Financial Officer</p>
    </div>
    <ul class="contact-list">
      <li class="contact-list__item">
        <svg class="contact-list__icon" viewBox="0 0 24 24" aria-hidden="true">
          <circle cx="12" cy="12" r="11" fill="var(--navy)"/>
          <path d="M8.2 6.5l2 2.6-1.2 1.5c.8 1.8 2.3 3.3 4.1 4.1l1.5-1.2 2.6 2-1.3 2c-4.8-.6-8.6-4.4-9.2-9.2z" fill="#fff"/>
        </svg>(555) 817-3094
      </li>
      <li class="contact-list__item">
        <svg class="contact-list__icon" viewBox="0 0 24 24" aria-hidden="true">
          <circle cx="12" cy="12" r="10.5" fill="none" stroke="var(--navy)" stroke-width="1.6"/>
          <rect x="6" y="8" width="12" height="8.5" fill="none" stroke="var(--navy)" stroke-width="1.3"/>
          <path d="M6 8l6 5 6-5M6 16.5l4.5-4M18 16.5l-4.5-4" fill="none" stroke="var(--navy)" stroke-width="1.1"/>
        </svg>larkridgemgmt.example
      </li>
      <li class="contact-list__item">
        <svg class="contact-list__icon" viewBox="0 0 24 24" aria-hidden="true">
          <circle cx="12" cy="12" r="10.5" fill="none" stroke="var(--navy)" stroke-width="1.6"/>
          <circle cx="12" cy="12" r="6.5" fill="none" stroke="var(--navy)" stroke-width="1.2"/>
          <ellipse cx="12" cy="12" rx="3" ry="6.5" fill="none" stroke="var(--navy)" stroke-width="1.1"/>
          <path d="M5.5 12h13M6.5 9h11M6.5 15h11" stroke="var(--navy)" stroke-width="1"/>
        </svg>www.larkridgemgmt.example
      </li>
    </ul>
    <div class="base-band"></div>
  </section>

</main>
</body>
</html>
```